Business Card Design for Oncology Consulting Company

We need a business card design using a logo that has already been created.

Company name is: WMBHO - Guild for Tumor Projection, Therapy and Remediation

We would also like to include the following pieces of information on the business card:
Name
Title
US Address (street, city, state, zip, country)
Email address
Website address

Target Market(s)

The target customers are physicians (oncologists, pathologists) in Greece, Iran, US, etc who would refer patients to our company for a second medical opinion/genetic counseling for cancer.

Industry/Entity Type

Business

Colors

Designer to choose colors to be used in the design.

Requirements
Must have
• Must contain logo in attached file and elements described above.

```html
<!DOCTYPE html>
<html lang="en">
<head>
<meta charset="utf-8">
<title>WMBHO Business Card</title>
<link href="https://fonts.googleapis.com/css2?family=Ubuntu:wght@400;500&display=swap" rel="stylesheet">
<style>
  :root {
    --brand-blue: #1f62ad;
    --ink: #2b2b2b;
    --muted: #8a8f96;
    --paper: #ffffff;
    --tagline-light: #dfe8f4;
    --backdrop: #e6e7e9;
  }
  * { margin: 0; padding: 0; box-sizing: border-box; }
  html, body {
    width: 1200px; height: 960px; overflow: hidden;
    background: var(--backdrop);
    font-family: "Ubuntu", sans-serif;
  }
  .sheet {
    width: 1200px; height: 960px;
    display: flex; flex-direction: column; align-items: center; justify-content: center;
    gap: 60px;
  }
  .card {
    position: relative;
    width: 700px; height: 400px;
    box-shadow: 0 6px 18px rgba(0,0,0,0.12);
    overflow: hidden;
  }
  .card--front { background: var(--paper); color: var(--ink); }
  .card--back { background: var(--brand-blue); color: var(--paper); }

  .brand { position: absolute; display: flex; flex-direction: column; }
  .brand__row { display: flex; align-items: center; gap: 14px; }
  .brand__name { font-weight: 400; letter-spacing: 3px; line-height: 1; }
  .brand__dot { width: 16px; height: 16px; border-radius: 50%; }
  .brand__tagline {
    font-size: 10px; font-weight: 400; text-transform: uppercase; letter-spacing: 0.6px;
    margin-top: 12px; padding-top: 5px;
    border-top: 1px solid currentColor;
    white-space: nowrap;
  }

  .card--front .brand { left: 48px; top: 70px; }
  .card--front .brand__name { font-size: 76px; color: var(--brand-blue); }
  .card--front .brand__dot { background: var(--brand-blue); }
  .card--front .brand__tagline { color: var(--muted); }

  .card--back .brand { left: 80px; top: 140px; }
  .card--back .brand__name { font-size: 88px; color: var(--paper); }
  .card--back .brand__dot { background: var(--paper); }
  .card--back .brand__tagline { color: var(--tagline-light); font-size: 11px; }

  .person { position: absolute; left: 48px; top: 250px; }
  .person__name { font-size: 32px; font-weight: 400; }
  .person__title { font-size: 19px; margin-top: 4px; margin-left: 8px; }

  .contact {
    position: absolute; left: 392px; top: 220px;
    list-style: none; font-size: 17px; line-height: 1.2;
  }
  .contact__item { display: flex; align-items: flex-start; gap: 12px; margin-bottom: 9px; white-space: nowrap; }
  .contact__icon { width: 24px; height: 24px; flex: none; }
</style>
</head>
<body>
<main class="sheet">

  <section class="card card--front" aria-label="Business card front">
    <div class="brand">
      <div class="brand__row">
        <span class="brand__name">WMBHO</span>
        <span class="brand__dot"></span>
      </div>
      <span class="brand__tagline">Guild for Tumor Projection, Therapy and Remediation</span>
    </div>

    <div class="person">
      <p class="person__name">Daniel Reyes</p>
      <p class="person__title">Manager</p>
    </div>

    <ul class="contact">
      <li class="contact__item">
        <svg class="contact__icon" viewBox="0 0 24 24"><circle cx="12" cy="12" r="12" fill="#1f62ad"/><path d="M8 6.5l2.2 0.3 0.8 2.8-1.3 1a7 7 0 0 0 3.7 3.7l1-1.3 2.8 0.8 0.3 2.2c-5 1-10.5-4.5-9.5-9.5z" fill="#fff"/></svg>
        <span>(617) 555 0142</span>
      </li>
      <li class="contact__item">
        <svg class="contact__icon" viewBox="0 0 24 24"><circle cx="12" cy="12" r="12" fill="#1f62ad"/><rect x="6" y="8" width="12" height="8.5" fill="#fff"/><path d="M6 8l6 5 6-5" fill="none" stroke="#1f62ad" stroke-width="1.2"/></svg>
        <span>daniel.reyes@wmbho.com</span>
      </li>
      <li class="contact__item">
        <svg class="contact__icon" viewBox="0 0 24 24"><circle cx="12" cy="12" r="12" fill="#1f62ad"/><path d="M12 5a4.5 4.5 0 0 0-4.5 4.5c0 3.3 4.5 9 4.5 9s4.5-5.7 4.5-9A4.5 4.5 0 0 0 12 5z" fill="#fff"/><circle cx="12" cy="9.5" r="1.7" fill="#1f62ad"/></svg>
        <span>245 Harbor Street<br>Boston, MA 02110, USA</span>
      </li>
      <li class="contact__item">
        <svg class="contact__icon" viewBox="0 0 24 24"><circle cx="12" cy="12" r="12" fill="#1f62ad"/><rect x="8.5" y="5.5" width="7" height="13" rx="3.5" fill="#fff"/><line x1="12" y1="6" x2="12" y2="10" stroke="#1f62ad" stroke-width="1.2"/></svg>
        <span>www.wmbho.com</span>
      </li>
    </ul>
  </section>

  <section class="card card--back" aria-label="Business card back">
    <div class="brand">
      <div class="brand__row">
        <span class="brand__name">WMBHO</span>
        <span class="brand__dot"></span>
      </div>
      <span class="brand__tagline">Guild for Tumor Projection, Therapy and Remediation</span>
    </div>
  </section>

</main>
</body>
</html>
```